依頼詳細
鹿児島県内で介護事業を展開しております、株式会社KMRと申します。
募集をご覧いただき、ありがとうございます。

▶弊社ホームへ―ジ◀
https://www.hinata-kmr-sample.com/

弊社が運営する「サービス付き高齢者向け住宅」の新聞折込用チラシ作成の依頼になります。過去に作成したチラシをリニューアルする目的で募集をかけました。高所得者層へ訴求効果の高いデザインおよび文書を構成し、チラシデータの作成をお願いします。

◆経緯
昨年、鹿児島の市街地にサービス付き高齢者向け住宅をオープンしました。これまで展開してきた施設とはターゲット層が異なるため、弊社保有のノウハウでは訴求効果が得られず、以下の要項での募集に至りました。

◆完成イメージ・目的
・「サービス付き高齢者向け住宅」の入居獲得を目的としたチラシ。
・「高所得者層」へ訴求効果の高いデザイン構成。
・高級分譲マンションのチラシのような完成イメージ。
・過去に制作したチラシをリニューアルする。
・新デザインのチラシを再配布し、顧客獲得を目的とする。
・ウェブサイトに掲載する素材としても活用できると良い。

◆応募条件・内容
・上記完成イメージに近い制作実績をお持ちの方。
・今回は単発での依頼ですが、スキルを拝見し、今後プロジェクト方式での継続発注も視野に入れています。

何かご不明点あれば、お気軽にお問い合わせくださいませ。
記載項目
・添付データにあります、「結縁ハウスこもれび西川町パンフ」に記載のある内容をベースに作成をお願いします。(※3ページ目の「デイサービスセンター」「共同生活援助」の項目は不要です)
・「共生ホーム」という表現は使わず、「サービス付き高齢者向け住宅」の表現に統一してください。
サイズ
B5
ページ数
両面
希望イメージ
シンプル 複雑
単色 カラフル
暗い 明るい
日常 高級
遊び心 厳粛
未来的 伝統的
女性的 男性的
希望する色
水色系、無彩色系、ゴールド系
納品ファイル
• イラストレーター形式 (.ai)
補足説明
※データ容量の問題で添付ファイルにaiファイルを含めてアップすることができませんでした。以下のリンクからダウンロードお願いします。
https://files.example-share.net/folders/7-Qwm2LpR8bv4TyeKd9Nx0sWfJ?usp=sharing
依頼公開後の追記内容
[2/26 23:15追記]
要望がありましたので、リンク先のaiファイルをCS6のバージョンに差し替えました。
[3/2 14:35追記]
リンク先のフォルダに画像素材の追加をおこないましたので、ご確認頂けばと思います。
引き続き、よろしくお願い致します。
[3/2 18:30追記]
・提供した素材の中に「音声記録システム」に関する記載があるのですが、そちらの記載は不要です(予め伝えておらす申し訳ないです)

・提供した素材の中に「青の3本縦ラインのロゴのようなもの」がありますが、そちらは特に意味のあるものではありませんので、デザインに入れなくて結構です。
■ 選んだ理由

高級分譲マンションの様なイメージ、かつ高齢者向け住宅であることがわかるイメージがバランス良くデザインに表現されているということで、結果として社内検討の多数決で決定いたしました。

■ 提案者全員のお礼・コメント

この度はたくさんの提案を頂き有難うございました。
想定していたよりも良い提案をたくさんいただき、また、それぞれの提案に魅力があり、選定するのが難しいでした。
今回、当選されなかった方も、また機会がありましたら何らかの形で依頼ができればと考えています。有難うございました。

```html
<!DOCTYPE html>
<html lang="ja">
<head>
<meta charset="utf-8">
<title>こもれび西川町 ご案内チラシ</title>
<link href="https://fonts.googleapis.com/css2?family=Shippori+Mincho:wght@400;600&family=Cormorant+Garamond:wght@400;500&family=Josefin+Sans:wght@400;500&family=Great+Vibes&display=swap" rel="stylesheet">
<style>
:root{
  --navy:#1f2d4d;
  --navy-deep:#17223c;
  --ink:#2a3550;
  --gold:#c9a55a;
  --gold-soft:#dcc48c;
  --paper:#ffffff;
  --plan:#eef0f3;
}
*{margin:0;padding:0;box-sizing:border-box}
html,body{width:848px;height:1200px;overflow:hidden;background:var(--paper)}
.flyer{position:relative;width:848px;height:1200px;overflow:hidden;background:var(--paper);font-family:"Shippori Mincho",serif;color:var(--ink)}
.floor-plan{position:absolute;left:420px;top:440px;width:428px;height:168px;background:linear-gradient(180deg,#f6f7f9 0%,var(--plan) 100%)}
.hero-photo{position:absolute;left:42px;top:0;width:548px;height:392px;background:linear-gradient(135deg,#f4f5f6 0%,#e5e8ec 55%,#cfd4da 100%);box-shadow:0 6px 14px rgba(0,0,0,.14)}
.brand{position:absolute;right:30px;top:34px;text-align:center;color:var(--navy)}
.brand-name{font-family:"Cormorant Garamond",serif;font-size:40px;font-weight:500;letter-spacing:3px;line-height:1}
.brand-sub{font-family:"Cormorant Garamond",serif;font-size:10px;letter-spacing:2px;margin-top:4px}
.tagline{position:absolute;right:60px;top:112px;writing-mode:vertical-rl;font-size:28px;line-height:1.6;letter-spacing:2px;color:var(--ink);font-weight:600}
.title{position:absolute;left:42px;top:400px;font-family:"Josefin Sans",sans-serif;color:var(--navy);font-size:34px;letter-spacing:5px;line-height:70px;font-weight:500}
.title .debut{display:flex;align-items:baseline;gap:16px}
.title .debut small{font-family:"Cormorant Garamond",serif;font-size:13px;letter-spacing:1px;font-weight:400}
.invite{position:absolute;left:0;top:608px;width:848px;height:592px;background:linear-gradient(180deg,var(--navy) 0%,var(--navy-deep) 100%)}
.building{position:absolute;left:0;top:660px;width:360px;height:540px;background:linear-gradient(160deg,#f2f4f7 0%,#c9d1dc 60%,#8e9bb0 100%);clip-path:polygon(0 14%,62% 0,100% 6%,100% 100%,0 100%)}
.seal{position:absolute;left:376px;top:866px;width:78px;height:78px;background:linear-gradient(135deg,var(--gold-soft),var(--gold))}
.script{position:absolute;left:430px;top:880px;font-family:"Great Vibes",cursive;font-size:54px;line-height:1;color:var(--gold-soft)}
.headline{position:absolute;left:368px;top:972px;width:420px;font-size:25px;font-weight:400;color:#fff;letter-spacing:2px;padding-bottom:10px;border-bottom:1px solid var(--gold)}
.lead{position:absolute;left:368px;top:1030px;font-size:12px;color:#e6e9ef;letter-spacing:1px}
.guide{position:absolute;left:368px;top:1080px;color:#fff}
.guide .kind{font-size:12px;letter-spacing:1px}
.guide .name{font-size:21px;letter-spacing:2px;margin-top:4px}
.guide .url{font-family:"Cormorant Garamond",serif;font-size:12px;margin-top:6px;color:#dfe3ea}
</style>
</head>
<body>
<div class="flyer">
  <div class="floor-plan" role="img" aria-label="住宅の間取り図"></div>
  <div class="hero-photo" role="img" aria-label="明るい寝室で両腕を伸ばして目覚める高齢の女性の写真"></div>
  <div class="brand">
    <div class="brand-name">KMR</div>
    <div class="brand-sub">KMR CARE GROUP</div>
  </div>
  <p class="tagline">「こもれび西川町」が贈る<br>高齢者向け住宅の新たな快適</p>
  <h1 class="title">
    KOMOREBI<br>NISHIKAWAMACHI
    <span class="debut">DEBUT <small>Serviced housing for the elderly</small></span>
  </h1>
  <section class="invite"></section>
  <div class="building" role="img" aria-label="白い外壁の高層住宅の外観写真"></div>
  <div class="seal" role="img" aria-label="金色の封蝋の装飾"></div>
  <div class="script">invitation</div>
  <h2 class="headline">上質な快適を求めている皆様へ</h2>
  <p class="lead">安心とくつろぎの暮らしがここにあります。</p>
  <div class="guide">
    <p class="kind">サービス付き高齢者向け住宅</p>
    <p class="name">「こもれび西川町」のご案内</p>
    <p class="url">https://www.hinata-kmr-sample.com/</p>
  </div>
</div>
</body>
</html>
```